House-share and Room Rental Website (With Focus on the Bedroom Landing Page)

Looking for website design for our House-share (executive accommodation) and room rental business.

Our company name is: Lodvenra could also be written as LodVenra or lodvenra. Either is fine .. just looking for a nice clean catchy logo to go with the design.

EXAMPLES
These are examples of other websites in this field that are doing well. this is a kind of baseline.
https://kelbrin.com.au/
https://www.tuvaplex.com/
https://www.nestorvi.com/
https://www.quillsa.net/
https://www.pendlebarrow.com.au/

Our business model is to rent rooms to people looking for high-quality accommodation. We fill the gap between those looking to rent rooms and those with rooms to rent. However, our model is slightly different from those already on the market as we looking to fill a massive gap in the market delivering upmarket rooms for rent.(Executive Accommodation) also in the back end will be coupled with a self management process in the back end.

We offer executive style accommodation that stands out above the rest. With special extras like fire safety.. and management processes that create happier homes. We are looking for a web design package that can help us grow and scale our business. We need a design that is captivating

Our MAIN focus is having a room landing page that stands out from the rest... The core of our business will rely on the promotion of the rooms in a share house... so the whole design relies on the BEDROOM landing page to drive results.

Target Market(s)

We have 2 markets we are aiming at ... the first market is people offering rooms to rent who want the highest rental return. The second market is people looking to rent safe, high-quality rooms, in houses that are well managed and looked after.

Industry/Entity Type

Share Economy

Logo Text

LodVenra

Number of Pages Required

5+ page

Font styles to use
Sans Serif

Colors
3276b5

Requirements
Must have
• A messaging system whereby we can create direct communication between those offering rooms and those looking for rooms.
• A call to action that says " Schedule an Inspection"
• Landing page for promoting rooms
• A home page for showing stock.
• Profile page for those selling rooms
• Profile page for those looking for rooms.
• A scheduling calendar for booking inspections
Nice to have
• Pages where new residents can lock in a room.. pay bond and rents.. and sign contracts
• Notifications
• SMS capabilities in the backend.
Should not have
• No script or handwriting fonts.

```html
<!DOCTYPE html>
<html lang="en">
<head>
<meta charset="utf-8">
<title>lodvenra – Room Rental</title>
<link rel="stylesheet" href="https://fonts.googleapis.com/css2?family=Montserrat:wght@500;600;700&family=Lato:wght@400;700&display=swap">
<style>
:root{
  --brand:#3276b5;
  --ink:#111111;
  --dark:#0b0b0b;
  --text:#2b2b2b;
  --muted:#8a8a8a;
  --light:#ffffff;
  --line:#d6d6d6;
  --spec:#9a9a9a;
}
*{margin:0;padding:0;box-sizing:border-box}
html,body{width:1200px;height:3782px;overflow:hidden}
body{position:relative;background:var(--light);font-family:"Lato",sans-serif;color:var(--text)}
.abs{position:absolute}

/* header */
.site-header{left:0;top:0;width:1200px;height:100px;background:var(--dark)}
.brand{left:80px;top:24px;display:flex;align-items:center;gap:12px}
.brand-mark{width:40px;height:40px;border-radius:50%;background:var(--brand)}
.brand-text{display:flex;flex-direction:column}
.brand-tag{font-size:9px;letter-spacing:2px;color:var(--brand);font-weight:700}
.brand-name{font-size:32px;font-weight:700;color:var(--light);line-height:1}
.main-nav{left:444px;top:41px;display:flex;gap:27px;font-size:14px;color:var(--light);text-transform:uppercase}
.main-nav .active{color:var(--brand)}
.login-btn{left:988px;top:28px;width:134px;height:46px;background:var(--brand);color:var(--light);font-size:17px;display:flex;align-items:center;justify-content:center;letter-spacing:1px}

/* hero */
.hero{left:0;top:100px;width:1200px;height:525px;background:var(--dark)}
.hero-photo{left:83px;top:0;width:1117px;height:525px;
  background:
    radial-gradient(ellipse 260px 200px at 160px 170px,rgba(240,244,242,.95),rgba(240,244,242,0)),
    radial-gradient(ellipse 200px 120px at 640px 260px,rgba(40,52,82,.55),rgba(40,52,82,0)),
    radial-gradient(ellipse 260px 140px at 930px 350px,rgba(150,152,156,.8),rgba(150,152,156,0)),
    linear-gradient(90deg,#c9cfcc 0%,#e6e8e5 25%,#cbb9a6 48%,#e3e1dc 62%,#cfcdc8 80%,#a9a7a2 100%)}
.hero-shade{left:83px;top:0;width:1117px;height:525px;background:linear-gradient(180deg,rgba(0,0,0,.05) 35%,rgba(0,0,0,.6) 100%)}
.hero-dots{left:36px;top:198px;display:flex;flex-direction:column;gap:10px}
.hero-dots span{width:14px;height:14px;border:2px solid var(--light);border-radius:50%}
.hero-dots span.on{background:var(--light)}
.hero-title{left:128px;top:318px;font-family:"Montserrat",sans-serif;font-weight:600;font-size:42px;color:var(--light)}
.hero-copy{left:128px;top:390px;width:820px;font-size:18px;line-height:28px;color:var(--light)}

/* listings */
.listing{width:322px;height:514px}
.listing-photo{left:0;top:0;width:322px;height:416px}
.photo-yellow{background:
  radial-gradient(ellipse 90px 60px at 120px 80px,rgba(255,232,160,.9),rgba(255,232,160,0)),
  radial-gradient(ellipse 180px 90px at 200px 300px,rgba(232,178,28,1),rgba(232,178,28,0)),
  radial-gradient(ellipse 110px 80px at 40px 250px,rgba(70,90,170,.9),rgba(70,90,170,0)),
  linear-gradient(180deg,#4b3a24 0%,#8d7348 35%,#c9a24a 60%,#dcab2a 80%,#b9892a 100%)}
.photo-hall{background:
  radial-gradient(ellipse 70px 160px at 160px 150px,rgba(250,246,238,1),rgba(250,246,238,0)),
  linear-gradient(90deg,#262320 0%,#3d3833 28%,#e9e3d8 48%,#f4efe6 58%,#6d5240 78%,#3a2a20 100%)}
.photo-sofa{background:
  radial-gradient(ellipse 160px 50px at 190px 240px,rgba(70,70,72,.95),rgba(70,70,72,0)),
  linear-gradient(180deg,#ecebe8 0%,#e2e0dc 50%,#7a7876 62%,#a8a6a3 78%,#cfcdca 100%)}
.listing-card{left:13px;top:283px;width:296px;height:227px;background:var(--light);box-shadow:0 4px 14px rgba(0,0,0,.12);padding:20px 16px 0}
.listing-title{font-size:15px;color:var(--ink)}
.listing-sub{font-size:13px;color:var(--text);margin-top:10px}
.listing-desc{font-size:13px;line-height:20px;color:var(--muted);margin-top:14px}
.listing-facts{display:flex;justify-content:space-between;margin-top:18px;font-size:13px;color:var(--muted)}
.fact{display:flex;align-items:center;gap:10px}
.fact svg{width:28px;height:20px;stroke:var(--muted);fill:none;stroke-width:1.5}

/* rooms */
.rooms{left:0;top:1873px;width:1200px;height:711px;background:var(--dark);color:var(--light)}
.rooms-title{left:80px;top:60px;font-family:"Montserrat",sans-serif;font-weight:600;font-size:42px}
.rooms-meta{top:130px;font-family:"Montserrat",sans-serif;font-size:17px;line-height:30px;font-weight:500}
.spec{font-size:15px}
.spec small{display:block;font-size:13px;color:var(--spec);margin-top:8px}
.room-photo{left:532px;top:222px;width:585px;height:396px;background:
  radial-gradient(ellipse 90px 60px at 390px 80px,rgba(90,160,190,.95),rgba(190,70,80,.5) 60%,rgba(0,0,0,0)),
  radial-gradient(ellipse 70px 50px at 30px 290px,rgba(200,30,40,.95),rgba(200,30,40,0)),
  radial-gradient(ellipse 170px 60px at 330px 260px,rgba(245,245,245,.95),rgba(245,245,245,0)),
  radial-gradient(ellipse 80px 40px at 320px 320px,rgba(110,180,200,.9),rgba(110,180,200,0)),
  linear-gradient(90deg,#eeeeec 0%,#e3e2df 40%,#2e2c2d 55%,#252324 85%,#3a3637 100%)}
.room-photo::after{content:"";position:absolute;left:0;right:0;bottom:0;height:60px;background:linear-gradient(90deg,#d9d9d9,#2a2a2a,#d9d9d9,#2a2a2a,#d9d9d9)}
.room-next{left:1147px;top:222px;width:53px;height:396px;background:linear-gradient(180deg,#6a6866 0%,#3a3838 60%,#c8c6c2 100%)}
.room-arrow{left:1037px;top:590px;width:54px;height:54px;border-radius:50%;background:var(--brand)}
.room-pager{left:532px;top:630px;display:flex;gap:26px}

/* question */
.question-photo{left:78px;top:2667px;width:456px;height:446px;background:
  radial-gradient(ellipse 120px 70px at 130px 290px,rgba(225,228,232,.95),rgba(225,228,232,0)),
  radial-gradient(ellipse 90px 120px at 270px 250px,rgba(170,190,215,.9),rgba(170,190,215,0)),
  radial-gradient(ellipse 140px 60px at 230px 390px,rgba(190,160,130,.9),rgba(190,160,130,0)),
  linear-gradient(180deg,#9c5a3a 0%,#c8967a 30%,#e6d2bf 48%,#6a6560 72%,#2e2c2b 100%)}
.question-title{left:630px;top:2690px;font-family:"Montserrat",sans-serif;font-weight:600;font-size:42px;color:var(--ink)}
.field{left:633px;width:446px;height:44px;border:1px solid var(--line);font-size:13px;color:var(--muted);padding:12px 16px}
.send-btn{left:633px;top:3038px;width:166px;height:45px;background:var(--brand);color:var(--light);font-family:"Montserrat",sans-serif;font-weight:600;font-size:18px;letter-spacing:1px;display:flex;align-items:center;justify-content:center}

/* schedule */
.schedule{left:0;top:3197px;width:1200px;height:496px;background:
  radial-gradient(ellipse 200px 80px at 1000px 370px,rgba(248,248,248,.95),rgba(248,248,248,0)),
  radial-gradient(ellipse 160px 160px at 120px 260px,rgba(120,120,118,.45),rgba(120,120,118,0)),
  linear-gradient(180deg,rgba(0,0,0,0) 80%,rgba(60,60,62,.7) 100%),
  linear-gradient(90deg,#e9eae8 0%,#d8d9d6 30%,#dcdad5 55%,#cfb28a 75%,#b89a72 100%)}
.schedule-panel{left:323px;top:121px;width:554px;height:312px;background:rgba(255,255,255,.85);text-align:center}
.schedule-title{margin-top:62px;font-family:"Montserrat",sans-serif;font-weight:600;font-size:32px;color:var(--ink)}
.schedule-copy{width:420px;margin:22px auto 0;font-size:17px;line-height:28px;color:var(--text)}
.schedule-btn{display:inline-flex;margin-top:26px;width:209px;height:43px;background:var(--brand);color:var(--light);font-size:16px;font-weight:700;letter-spacing:1px;align-items:center;justify-content:center}
.chat-btn{left:1066px;top:3672px;width:52px;height:52px;border-radius:50%;background:var(--brand);display:flex;align-items:center;justify-content:center}

.site-footer{left:80px;top:3732px;font-size:14px;color:var(--text)}
</style>
</head>
<body>

<header class="abs site-header">
  <div class="abs brand">
    <span class="brand-mark"></span>
    <span class="brand-text"><span class="brand-tag">ROOM RENTAL</span><span class="brand-name">lodvenra</span></span>
  </div>
  <nav class="abs main-nav">
    <span class="active">Home</span><span>Rooms</span><span>Sellers</span><span>Rentors</span><span>Schedule an Inspection</span>
  </nav>
  <div class="abs login-btn">LOGIN</div>
</header>

<section class="abs hero">
  <div class="abs hero-photo" role="img" aria-label="Bright modern bedroom with balcony window, navy cushions and grey sofa"></div>
  <div class="abs hero-shade"></div>
  <div class="abs hero-dots"><span class="on"></span><span></span><span></span><span></span></div>
  <h1 class="abs hero-title">find your place with our local life style</h1>
  <p class="abs hero-copy">Lorem Ipsum is simply dummy text of the printing and typesetting industry. Lorem Ipsum has been the industry's standard dummy text ever since the 1500s, when an unknown printer.</p>
</section>

<div class="abs listing" style="left:78px;top:708px">
  <div class="abs listing-photo photo-yellow" role="img" aria-label="Bedroom with yellow bedspread and pendant lights"></div>
  <div class="abs listing-card"><p class="listing-title">Lorem Ipsum is simply dummy text.</p><p class="listing-sub">Lorem Ipsum is simply dummy text.</p><p class="listing-desc">Lorem Ipsum is simply dummy text of the printing and typesetting industry. Lorem Ipsum has been the industry's standard.</p>
  <div class="listing-facts"><span class="fact"><svg viewBox="0 0 28 20"><path d="M2 18V4M2 12h24v6M26 12V9a3 3 0 0 0-3-3H11v6M5 10h4"/></svg>02</span><span class="fact"><svg viewBox="0 0 28 20"><path d="M3 9h22l-2 7H5zM7 16l-1 3M21 16l1 3M6 9V4a2 2 0 0 1 4 0"/></svg>01</span><span class="fact"><svg viewBox="0 0 28 20"><path d="M3 18h22L19 4H9zM9 12h10M14 4v14"/></svg>02</span></div></div>
</div>
<div class="abs listing" style="left:439px;top:708px">
  <div class="abs listing-photo photo-hall" role="img" aria-label="Bright hallway with patterned screen and wooden wardrobe"></div>
  <div class="abs listing-card"><p class="listing-title">Lorem Ipsum is simply dummy text.</p><p class="listing-sub">Lorem Ipsum is simply dummy text.</p><p class="listing-desc">Lorem Ipsum is simply dummy text of the printing and typesetting industry. Lorem Ipsum has been the industry's standard.</p>
  <div class="listing-facts"><span class="fact"><svg viewBox="0 0 28 20"><path d="M2 18V4M2 12h24v6M26 12V9a3 3 0 0 0-3-3H11v6M5 10h4"/></svg>02</span><span class="fact"><svg viewBox="0 0 28 20"><path d="M3 9h22l-2 7H5zM7 16l-1 3M21 16l1 3M6 9V4a2 2 0 0 1 4 0"/></svg>01</span><span class="fact"><svg viewBox="0 0 28 20"><path d="M3 18h22L19 4H9zM9 12h10M14 4v14"/></svg>02</span></div></div>
</div>
<div class="abs listing" style="left:799px;top:708px">
  <div class="abs listing-photo photo-sofa" role="img" aria-label="Grey sofa with patterned cushions against a white wall"></div>
  <div class="abs listing-card"><p class="listing-title">Lorem Ipsum is simply dummy text.</p><p class="listing-sub">Lorem Ipsum is simply dummy text.</p><p class="listing-desc">Lorem Ipsum is simply dummy text of the printing and typesetting industry. Lorem Ipsum has been the industry's standard.</p>
  <div class="listing-facts"><span class="fact"><svg viewBox="0 0 28 20"><path d="M2 18V4M2 12h24v6M26 12V9a3 3 0 0 0-3-3H11v6M5 10h4"/></svg>02</span><span class="fact"><svg viewBox="0 0 28 20"><path d="M3 9h22l-2 7H5zM7 16l-1 3M21 16l1 3M6 9V4a2 2 0 0 1 4 0"/></svg>01</span><span class="fact"><svg viewBox="0 0 28 20"><path d="M3 18h22L19 4H9zM9 12h10M14 4v14"/></svg>02</span></div></div>
</div>

<div class="abs listing" style="left:78px;top:1281px">
  <div class="abs listing-photo photo-yellow" role="img" aria-label="Bedroom with yellow bedspread and pendant lights"></div>
  <div class="abs listing-card"><p class="listing-title">Lorem Ipsum is simply dummy text.</p><p class="listing-sub">Lorem Ipsum is simply dummy text.</p><p class="listing-desc">Lorem Ipsum is simply dummy text of the printing and typesetting industry. Lorem Ipsum has been the industry's standard.</p>
  <div class="listing-facts"><span class="fact"><svg viewBox="0 0 28 20"><path d="M2 18V4M2 12h24v6M26 12V9a3 3 0 0 0-3-3H11v6M5 10h4"/></svg>02</span><span class="fact"><svg viewBox="0 0 28 20"><path d="M3 9h22l-2 7H5zM7 16l-1 3M21 16l1 3M6 9V4a2 2 0 0 1 4 0"/></svg>01</span><span class="fact"><svg viewBox="0 0 28 20"><path d="M3 18h22L19 4H9zM9 12h10M14 4v14"/></svg>02</span></div></div>
</div>
<div class="abs listing" style="left:439px;top:1281px">
  <div class="abs listing-photo photo-hall" role="img" aria-label="Bright hallway with patterned screen and wooden wardrobe"></div>
  <div class="abs listing-card"><p class="listing-title">Lorem Ipsum is simply dummy text.</p><p class="listing-sub">Lorem Ipsum is simply dummy text.</p><p class="listing-desc">Lorem Ipsum is simply dummy text of the printing and typesetting industry. Lorem Ipsum has been the industry's standard.</p>
  <div class="listing-facts"><span class="fact"><svg viewBox="0 0 28 20"><path d="M2 18V4M2 12h24v6M26 12V9a3 3 0 0 0-3-3H11v6M5 10h4"/></svg>02</span><span class="fact"><svg viewBox="0 0 28 20"><path d="M3 9h22l-2 7H5zM7 16l-1 3M21 16l1 3M6 9V4a2 2 0 0 1 4 0"/></svg>01</span><span class="fact"><svg viewBox="0 0 28 20"><path d="M3 18h22L19 4H9zM9 12h10M14 4v14"/></svg>02</span></div></div>
</div>
<div class="abs listing" style="left:799px;top:1281px">
  <div class="abs listing-photo photo-sofa" role="img" aria-label="Grey sofa with patterned cushions against a white wall"></div>
  <div class="abs listing-card"><p class="listing-title">Lorem Ipsum is simply dummy text.</p><p class="listing-sub">Lorem Ipsum is simply dummy text.</p><p class="listing-desc">Lorem Ipsum is simply dummy text of the printing and typesetting industry. Lorem Ipsum has been the industry's standard.</p>
  <div class="listing-facts"><span class="fact"><svg viewBox="0 0 28 20"><path d="M2 18V4M2 12h24v6M26 12V9a3 3 0 0 0-3-3H11v6M5 10h4"/></svg>02</span><span class="fact"><svg viewBox="0 0 28 20"><path d="M3 9h22l-2 7H5zM7 16l-1 3M21 16l1 3M6 9V4a2 2 0 0 1 4 0"/></svg>01</span><span class="fact"><svg viewBox="0 0 28 20"><path d="M3 18h22L19 4H9zM9 12h10M14 4v14"/></svg>02</span></div></div>
</div>

<section class="abs rooms">
  <h2 class="abs rooms-title">Rooms</h2>
  <p class="abs rooms-meta" style="left:80px;width:330px">Address : Lorem Ipsum is simply dummy text of the printing.</p>
  <p class="abs rooms-meta" style="left:492px">Rental price : $ 250</p>
  <p class="abs rooms-meta" style="left:800px;width:330px">utilities : included/excluded price of utilities</p>

  <p class="abs spec" style="left:80px;top:245px">Gender Preference<small>male/female</small></p>
  <p class="abs spec" style="left:287px;top:245px">Size of room<small>40 Sqm</small></p>
  <p class="abs spec" style="left:80px;top:321px">Bathroom<small>shared/private</small></p>
  <p class="abs spec" style="left:287px;top:321px">Parking<small>street/off-street/private</small></p>
  <p class="abs spec" style="left:80px;top:397px">Smoking/non-smoking<small>Smoking/non-smoking</small></p>
  <p class="abs spec" style="left:287px;top:397px">minimum contract ter<small>usually 3 months</small></p>
  <p class="abs spec" style="left:80px;top:473px">Bed size<small>male/female</small></p>
  <p class="abs spec" style="left:287px;top:473px">Type of housemates<small>Professionals/students</small></p>
  <p class="abs spec" style="left:80px;top:549px">room type<small>private/shared</small></p>
  <p class="abs spec" style="left:287px;top:549px">internet speed<small>12 Mbps</small></p>

  <div class="abs room-photo" role="img" aria-label="Bedroom with black feature wall, colourful artwork, red chair and black and white bedding"></div>
  <div class="abs room-next" role="img" aria-label="Next room photo"></div>
  <div class="abs room-arrow"><svg width="54" height="54" viewBox="0 0 54 54"><path d="M24 19l8 8-8 8" stroke="#fff" stroke-width="2.5" fill="none"/></svg></div>
  <div class="abs room-pager">
    <svg width="32" height="14" viewBox="0 0 32 14"><path d="M31 7H2M8 1L2 7l6 6" stroke="#3276b5" stroke-width="1.6" fill="none"/></svg>
    <svg width="32" height="14" viewBox="0 0 32 14"><path d="M1 7h29M24 1l6 6-6 6" stroke="#3276b5" stroke-width="1.6" fill="none"/></svg>
  </div>
</section>

<div class="abs question-photo" role="img" aria-label="Couple relaxing on a sofa with a laptop in front of a brick wall"></div>
<h2 class="abs question-title">Have a Question?</h2>
<div class="abs field" style="top:2763px">Name</div>
<div class="abs field" style="top:2818px">Email</div>
<div class="abs field" style="top:2873px">Phone</div>
<div class="abs field" style="top:2928px;height:96px">Your Question or Message</div>
<div class="abs send-btn">SEND</div>

<section class="abs schedule" role="img" aria-label="Bright bedroom with a bicycle, wooden wall and soft cushions">
  <div class="abs schedule-panel">
    <h2 class="schedule-title">Schedule an Inspection</h2>
    <p class="schedule-copy">Lorem Ipsum is simply dummy text of the printing and typesetting industry Lorem Ipsum</p>
    <span class="schedule-btn">SCHEDULE NOW</span>
  </div>
</section>
<div class="abs chat-btn"><svg width="26" height="22" viewBox="0 0 26 22"><path d="M2 2h14v9H7l-4 3v-3H2zM10 13v3h9l4 3v-3h1V7h-5" fill="#fff"/></svg></div>

<footer class="abs site-footer">©lodvenra. 2019 - All Rights Reserved.</footer>

</body>
</html>
```